Q-Rolls Business Card

We are a modern retail clothing store. Established in 1994. I need a presentable card that will amaze vendors when given to them.

Front: Logo in middle
Info Side:

Name: Tomas Velder
Cell: 630-812-4463
Work: 630-917-3384 EXT. 417
Email: Tomas@q-rolls-example.com
Website: www.Q-rolls-example.com

Industry/Entity Type

Business

```html
<!DOCTYPE html>
<html lang="en">
<head>
<meta charset="utf-8">
<title>Q-Rolls Business Card</title>
<link href="https://fonts.googleapis.com/css2?family=Roboto:wght@400;500;700&display=swap" rel="stylesheet">
<style>
  :root {
    --backdrop: #3a3431;
    --card: #161616;
    --card-edge: #0c0c0c;
    --gloss: #2b2b2b;
    --ink: #f2f2f2;
    --ink-soft: #cfcfcf;
  }
  * { margin: 0; padding: 0; box-sizing: border-box; }
  html, body {
    width: 1200px;
    height: 716px;
    overflow: hidden;
    background: var(--backdrop);
    font-family: "Roboto", Arial, sans-serif;
  }
  .stage {
    position: relative;
    width: 1200px;
    height: 716px;
    display: flex;
    align-items: center;
    justify-content: center;
    gap: 70px;
  }
  .card {
    position: relative;
    width: 500px;
    height: 286px;
    background: var(--card);
    border: 1px solid var(--card-edge);
    box-shadow: 0 12px 30px rgba(0,0,0,0.35);
  }
  .brand-name {
    font-family: "Roboto", Arial, sans-serif;
    font-weight: 700;
    letter-spacing: 1px;
    line-height: 1;
  }
  .card--front {
    display: flex;
    align-items: center;
    justify-content: center;
  }
  .card--front .brand-name {
    font-size: 44px;
    color: var(--gloss);
  }
  .card--info .brand-name {
    position: absolute;
    right: 40px;
    top: 104px;
    font-size: 34px;
    color: var(--ink);
  }
  .contact {
    position: absolute;
    left: 32px;
    top: 128px;
    color: var(--ink);
  }
  .contact__name {
    font-size: 15px;
    font-weight: 700;
    margin-bottom: 3px;
  }
  .contact__role {
    font-size: 10px;
    color: var(--ink-soft);
    margin-bottom: 10px;
  }
  .contact__list { list-style: none; }
  .contact__item {
    display: flex;
    align-items: center;
    gap: 7px;
    font-size: 11px;
    line-height: 17px;
    color: var(--ink);
  }
  .contact__item--split { gap: 7px; }
  .icon {
    width: 10px;
    height: 10px;
    flex: none;
    fill: none;
    stroke: var(--ink);
    stroke-width: 1.2;
  }
</style>
</head>
<body>
  <main class="stage">
    <section class="card card--front" aria-label="Card front">
      <span class="brand-name">Q-ROLLS</span>
    </section>

    <section class="card card--info" aria-label="Card back">
      <div class="contact">
        <p class="contact__name">Tomas Velder</p>
        <p class="contact__role">Managing Director</p>
        <ul class="contact__list">
          <li class="contact__item">
            <svg class="icon" viewBox="0 0 10 10" aria-hidden="true"><rect x="2.5" y="0.8" width="5" height="8.4" rx="0.8"/><line x1="4.3" y1="7.6" x2="5.7" y2="7.6"/></svg>
            630-812-4463
          </li>
          <li class="contact__item">
            <svg class="icon" viewBox="0 0 10 10" aria-hidden="true"><path d="M1 3.5 Q5 0.5 9 3.5 L8 4.5 L6.5 3.5 L3.5 3.5 L2 4.5 Z"/><rect x="2" y="5" width="6" height="4" rx="0.6"/></svg>
            630-917-3384 EXT. 417
          </li>
          <li class="contact__item contact__item--split">
            <svg class="icon" viewBox="0 0 10 10" aria-hidden="true"><rect x="0.8" y="2" width="8.4" height="6"/><polyline points="0.8,2 5,5.5 9.2,2"/></svg>
            Tomas@q-rolls-example.com
            <svg class="icon" viewBox="0 0 10 10" aria-hidden="true"><circle cx="5" cy="5" r="4.2"/><ellipse cx="5" cy="5" rx="1.8" ry="4.2"/><line x1="0.8" y1="5" x2="9.2" y2="5"/></svg>
            www.Q-rolls-example.com
          </li>
        </ul>
      </div>
      <span class="brand-name">Q-ROLLS</span>
    </section>
  </main>
</body>
</html>
```